Email Signature - GRAND HARBOUR STAYS DIRECT

Hi there,

I'm after an email signature for my email. I have attached a sample of what I like to this brief (File name: "Email Signature Sample").

I would like my email signature to have the following information:

Delphine Worrow
GRAND HARBOUR STAYS DIRECT
Mobile: 0431 792 046 ( Australia )
Tel: +61 431 792 046 ( International )
Email: delphine@grandharbourstaysdirect.example
Website: www.grandharbourstaysdirectexample

Industry/Entity Type

Online

Requirements
Must have
• I would like the signature to have a professional look

```html
<!DOCTYPE html>
<html lang="en">
<head>
<meta charset="utf-8">
<title>Delphine Worrow – Grand Harbour Stays Direct</title>
<link rel="stylesheet" href="https://fonts.googleapis.com/css2?family=Questrial&display=swap">
<style>
  :root {
    --ink: #111111;
    --paper: #ffffff;
    --blush: #fbc4bd;
    --rule: #000000;
  }
  * { margin: 0; padding: 0; box-sizing: border-box; }
  html, body {
    width: 1200px;
    height: 518px;
    overflow: hidden;
    background: var(--paper);
  }
  .signature {
    position: relative;
    width: 1200px;
    height: 518px;
    background: var(--paper);
    color: var(--ink);
    font-family: "Questrial", "Century Gothic", sans-serif;
  }
  .person-name {
    position: absolute;
    left: 64px;
    top: 52px;
    font-size: 41px;
    font-weight: 400;
    letter-spacing: 0.5px;
    line-height: 1;
  }
  .name-rule {
    position: absolute;
    left: 0;
    top: 111px;
    width: 383px;
    height: 2px;
    background: var(--rule);
  }
  .contact-list {
    position: absolute;
    left: 64px;
    top: 134px;
    list-style: none;
    font-size: 28px;
    line-height: 41.5px;
  }
  .contact-list .region {
    font-size: 21px;
  }
  .company-name {
    position: absolute;
    left: 48px;
    top: 366px;
    font-size: 36px;
    font-weight: 400;
    letter-spacing: 0.5px;
    line-height: 1;
    color: var(--ink);
  }
  .base-band {
    position: absolute;
    left: 0;
    top: 418px;
    width: 930px;
    height: 20px;
    background: var(--rule);
  }
  .brand-disc {
    position: absolute;
    left: 790px;
    top: 14px;
    width: 396px;
    height: 396px;
  }
</style>
</head>
<body>
  <div class="signature">
    <h1 class="person-name">Delphine Worrow</h1>
    <div class="name-rule"></div>

    <ul class="contact-list">
      <li>Mobile: 0431 792 046 <span class="region">(Australia)</span></li>
      <li>Tel: +61 431 792 046 <span class="region">(International)</span></li>
      <li>Chat: delphineworrow</li>
      <li>delphine@grandharbourstaysdirect.example</li>
      <li>www.grandharbourstaysdirectexample</li>
    </ul>

    <p class="company-name">GRAND HARBOUR STAYS DIRECT</p>
    <div class="base-band"></div>

    <svg class="brand-disc" viewBox="0 0 396 396" aria-hidden="true">
      <circle cx="198" cy="198" r="196" fill="var(--blush)"/>
    </svg>
  </div>
</body>
</html>
```